Orthodontist Needs Promotional Discount Postcard

5.5 x 8.5 Horizontal 2-Sided Postcard for mailing.
Images & Logo on both sides okay; must be free stock Images from legit sources only, or use attached images. See our website for information, CoveLineSmiles.com
Context to include:
New Patient Special $500 off Braces or Clear Aligners
Cannot be combined with any other discounts.
Major dental insurance plans and Vita-Plan accepted
Affordable payment options are available
Call to schedule your free consultation
Present this new patient offer to receive your discount.
Offer ends January 31, 2022.
805-419-2276 www. CoveLineSmiles.com
462 N. Marigold Street, Suite B, Ventura, CA 93001-5812
office@covelinesmiles.com

```html
<!DOCTYPE html>
<html lang="en">
<head>
<meta charset="utf-8">
<title>Cove Line Smiles – New Patient Postcard</title>
<link href="https://fonts.googleapis.com/css2?family=Antonio:wght@600;700&family=Montserrat:wght@400;500;600;700;800&display=swap" rel="stylesheet">
<style>
:root{
  --blue:#2a9fd8;
  --blue-deep:#1f86c0;
  --charcoal:#454647;
  --ink:#1b1b1b;
  --grey-bg:#a7a7a7;
  --panel-grey:#d9d9da;
  --white:#ffffff;
}
*{box-sizing:border-box;margin:0;padding:0}
html,body{width:1200px;height:2514px;overflow:hidden}
body{background:var(--grey-bg);font-family:"Montserrat",sans-serif;color:var(--ink);position:relative}
.card{position:absolute;left:40px;width:1120px;height:723px;background:var(--white);overflow:hidden;box-shadow:0 18px 20px -14px rgba(0,0,0,.45)}
.front{top:470px}
.back{top:1293px}

/* FRONT */
.hero{position:absolute;left:0;top:0;width:1120px;height:505px;background:linear-gradient(90deg,#f1f4f8 0%,#dfe9f2 55%,#eef3f8 100%)}
.hero-photo{position:absolute;left:0;top:0;width:610px;height:505px;background:radial-gradient(ellipse at 40% 45%,#e9c8b3 0%,#f3e7df 40%,#e6edf4 75%,rgba(228,237,245,0) 100%)}
.brand{position:absolute;left:530px;top:34px;width:590px;display:flex;align-items:center;justify-content:center;gap:18px}
.brand-dot{width:64px;height:64px;border-radius:50%;background:var(--blue)}
.brand-name{font-weight:600;font-size:42px;color:var(--blue);letter-spacing:2px;white-space:nowrap}
.doctor{position:absolute;left:530px;top:160px;width:590px;text-align:center;font-family:"Antonio",sans-serif;font-weight:700;font-size:60px;color:var(--blue);line-height:1;white-space:nowrap}
.specialty{position:absolute;left:600px;top:232px;width:450px;text-align:center;font-size:25px;font-weight:500;padding-bottom:10px;border-bottom:2px solid #8a8a8a;white-space:nowrap}
.intro{position:absolute;left:560px;top:296px;width:480px;font-size:14.5px;line-height:1.35}
.contact-box{position:absolute;left:570px;top:370px;width:430px;height:114px;border:2px solid var(--blue);border-radius:14px;background:var(--white)}
.contact-phone{position:absolute;left:22px;top:4px;display:flex;align-items:center;gap:6px;font-size:50px;color:var(--blue);font-weight:500;letter-spacing:1px;white-space:nowrap}
.contact-phone svg{width:38px;height:38px}
.contact-addr{position:absolute;left:20px;top:68px;display:flex;gap:8px;font-size:13px;line-height:1.3;white-space:nowrap}
.contact-web{position:absolute;left:262px;top:68px;display:flex;gap:6px;font-size:13px;align-items:center;white-space:nowrap}
.rule{position:absolute;left:0;top:505px;width:1120px;height:4px;background:var(--blue)}
.offers{position:absolute;left:48px;top:522px;width:1020px;display:flex;gap:10px}
.offer{flex:1;height:147px;background:var(--charcoal);border-radius:14px;outline:2px solid var(--charcoal);outline-offset:3px;border:2px solid #d0d0d0;color:var(--white);display:flex;flex-direction:column;align-items:center;justify-content:center;text-align:center;font-weight:600;font-size:22px;line-height:1.15;text-transform:uppercase}
.offer em{font-style:normal;color:var(--blue)}
.offer-head{font-size:20px;white-space:nowrap}
.offer-deal{display:flex;align-items:center;gap:12px;margin:6px 0}
.offer-amount{font-family:"Antonio",sans-serif;font-weight:700;font-size:54px;color:var(--blue);line-height:1;white-space:nowrap}
.offer-deal small{font-size:12px;font-weight:500;text-align:left;line-height:1.2;white-space:nowrap}
.offer-fine{font-size:10px;font-weight:500;white-space:nowrap}
.offer-big{font-size:27px;color:var(--blue)}
.deadline{position:absolute;left:0;top:679px;width:1120px;height:44px;background:var(--blue-deep);color:var(--white);font-size:20px;display:flex;align-items:center;justify-content:center;white-space:nowrap}
.deadline b{font-weight:700}

/* BACK */
.headline{position:absolute;left:0;top:0;width:1120px;height:78px;background:var(--blue);color:var(--white);font-weight:800;font-size:37px;display:flex;align-items:center;justify-content:center;letter-spacing:-1px;white-space:nowrap}
.portrait{position:absolute;left:41px;top:103px;width:163px;height:212px;background:linear-gradient(180deg,#9fbfd6 0%,#c9d3da 45%,#5e6a78 100%)}
.bio{position:absolute;left:226px;top:105px;width:323px}
.bio-label{font-weight:700;font-size:15px}
.bio-name{font-weight:700;font-size:22px;color:var(--blue);line-height:1}
.bio-tag{font-weight:700;font-size:15px;color:#333;margin-bottom:12px}
.bio p{font-size:11.3px;line-height:1.42;text-align:justify;color:#333}
.tech{position:absolute;left:39px;top:349px;width:369px;font-size:11.3px;line-height:1.42;color:#333}
.tech em{font-style:normal;font-weight:700;color:var(--blue)}
.features{position:absolute;left:41px;top:460px;width:370px;display:grid;grid-template-columns:205px 165px;row-gap:20px;font-size:13px;font-weight:600}
.feature{display:flex;align-items:center;gap:8px;white-space:nowrap}
.feature svg{width:22px;height:22px;fill:var(--blue)}
.robot{position:absolute;left:424px;top:346px;width:125px;height:187px;background:linear-gradient(180deg,#f1f1f1,#dcdcdc)}
.treatment{position:absolute;left:581px;top:103px;width:503px;height:196px;background:var(--blue);border-radius:16px;padding:6px 7px}
.treatment h3{color:var(--white);text-align:center;font-size:22px;font-weight:700;margin-bottom:6px}
.treatment-grid{display:flex;gap:8px}
.treatment-photo{flex:1;height:145px;position:relative;display:flex;align-items:flex-end;padding:6px 12px;color:var(--white);font-size:12px;font-weight:700}
.treatment-photo.traditional{background:linear-gradient(90deg,#c95a63,#e9d4cf 55%,#7b4d4a)}
.treatment-photo.aligners{background:linear-gradient(90deg,#f2dad2,#b2505b 60%,#e9c8be)}
.grey-side{position:absolute;left:529px;top:319px;width:591px;height:404px;background:var(--panel-grey)}
.white-notch{position:absolute;left:529px;top:319px;width:40px;height:230px;background:var(--white)}
.grey-foot{position:absolute;left:0;top:636px;width:1120px;height:87px;background:var(--panel-grey)}
.cta{position:absolute;left:0;top:549px;width:529px;height:87px;background:var(--blue);color:var(--white);padding:6px 22px}
.cta h4{font-size:21px;font-weight:700;letter-spacing:-.3px;white-space:nowrap}
.cta-row{display:flex;align-items:center;justify-content:space-between}
.cta-phone{display:flex;align-items:center;gap:6px;font-size:32px;font-weight:500;color:var(--ink);white-space:nowrap}
.cta-phone svg{width:26px;height:26px}
.cta-links{font-size:12.5px;color:var(--ink);line-height:1.3;white-space:nowrap}
</style>
</head>
<body>

<section class="card front">
  <div class="hero">
    <div class="hero-photo" role="img" aria-label="Photo of a smiling couple embracing"></div>
    <div class="brand"><span class="brand-dot"></span><span class="brand-name">COVE LINE SMILES</span></div>
    <h1 class="doctor">DANIEL K HALE, DDS, MS</h1>
    <p class="specialty">Certified Orthodontic Specialist</p>
    <p class="intro">While there are a lot of dentists doing orthodontic treatment, very few go on to do another 2-3 years of training and become a true specialist in orthodontics.</p>
    <div class="contact-box">
      <div class="contact-phone">
        <svg viewBox="0 0 24 24"><path fill="#555" d="M6.6 10.8a15.1 15.1 0 0 0 6.6 6.6l2.2-2.2c.3-.3.7-.4 1-.2 1.1.4 2.3.6 3.6.6.6 0 1 .4 1 1V20c0 .6-.4 1-1 1A17 17 0 0 1 3 4c0-.6.4-1 1-1h3.5c.6 0 1 .4 1 1 0 1.3.2 2.5.6 3.6.1.3 0 .7-.2 1z"/></svg>
        805 419 2276
      </div>
      <div class="contact-addr">
        <svg width="16" height="22" viewBox="0 0 16 22"><path fill="#2a9fd8" d="M8 0a8 8 0 0 0-8 8c0 6 8 14 8 14s8-8 8-14a8 8 0 0 0-8-8zm0 11a3 3 0 1 1 0-6 3 3 0 0 1 0 6z"/></svg>
        <span>462 N. Marigold St, Suite B,<br>Ventura, CA 93001</span>
      </div>
      <div class="contact-web">
        <svg width="15" height="15" viewBox="0 0 16 16"><circle cx="8" cy="8" r="7" fill="none" stroke="#2a9fd8" stroke-width="1.4"/><path d="M1 8h14M8 1c-3 3.5-3 10.5 0 14M8 1c3 3.5 3 10.5 0 14" fill="none" stroke="#2a9fd8" stroke-width="1.2"/></svg>
        covelinesmiles.com
      </div>
    </div>
  </div>
  <div class="rule"></div>
  <div class="offers">
    <div class="offer">
      <span class="offer-head">New Patient Special</span>
      <div class="offer-deal"><span class="offer-amount">$500 OFF</span><small>Braces or<br>Clear Aligners</small></div>
      <span class="offer-fine">Cannot be combined with any other discounts.</span>
    </div>
    <div class="offer">
      <span>Major <em>Dental</em><br><em>Insurance Plans</em> and<br><em>Vita-Plan</em> Accepted</span>
    </div>
    <div class="offer">
      <span class="offer-big">Affordable<br>Payment Options</span>
      <span>Are Available</span>
    </div>
  </div>
  <div class="deadline">PRESENT THIS NEW PATIENT OFFER TO RECEIVE YOUR DISCOUNT&nbsp;<b>| OFFER ENDS JANUARY 31, 2022.</b></div>
</section>

<section class="card back">
  <h2 class="headline">SUPERIOR TECHNOLOGY DEVELOPED RIGHT HERE</h2>
  <div class="portrait" role="img" aria-label="Portrait photo of the orthodontist on a beach"></div>
  <div class="bio">
    <div class="bio-label">THE ORTHODONTIST:</div>
    <div class="bio-name">DR HALE</div>
    <div class="bio-tag">INTERNATIONALLY RECOGNIZED</div>
    <p>Doctor Hale was born and raised in Southern California and received his Bachelor of Science in Biology from Seabright University, his Doctor of Dental Surgery from Pacific Coast University, and his Master of Science in Orthodontics and Dentofacial Orthopedics from Harborview University where he has been an Assistant Professor for the last 20 years.<br>Dr Hale has personally treated over <b>20,000</b> satisfied patients.</p>
  </div>
  <p class="tech"><em>True 3D treatment</em> planning was first on the list of changes that had to be made to better orthodontic treatment. In fact, Dr. Hale was on the team that brought the first <em>3D X-Ray Machine (Cone Beam)</em> into the United States, and the first orthodontist in the country to utilize this technology on every patient.</p>
  <div class="features">
    <div class="feature"><svg viewBox="0 0 24 24"><circle cx="8" cy="8" r="5"/><circle cx="16" cy="10" r="4"/><circle cx="10" cy="17" r="5"/></svg>3D Diagnosis</div>
    <div class="feature"><svg viewBox="0 0 24 24"><path d="M6 20h12v2H6zM9 18l3-8 5-3 2 2-4 5-4 4z"/><circle cx="8" cy="6" r="3"/></svg>Robotic Assistance</div>
    <div class="feature"><svg viewBox="0 0 24 24"><path d="M2 3h20v14H2zM8 19h8v2H8z"/><path d="M4 11h4l2-4 3 7 2-3h5" fill="none" stroke="#fff" stroke-width="1.5"/></svg>Virtual Appointments</div>
    <div class="feature"><svg viewBox="0 0 24 24"><path d="M7 2c-3 0-5 2-5 6 0 3 1 5 2 8l1 6h2l2-6h2l2 6h2l1-6c1-3 2-5 2-8 0-4-2-6-5-6-2 0-3 1-5 1S9 2 7 2z"/></svg>Advanced Brackets</div>
  </div>
  <div class="grey-side"></div>
  <div class="white-notch"></div>
  <div class="robot" role="img" aria-label="Photo of a white robotic arm"></div>
  <div class="treatment">
    <h3>TREATMENT TYPE</h3>
    <div class="treatment-grid">
      <div class="treatment-photo traditional" role="img" aria-label="Photo of a smile with traditional braces">TRADITIONAL</div>
      <div class="treatment-photo aligners" role="img" aria-label="Photo of a clear aligner being fitted">ALIGNERS</div>
    </div>
  </div>
  <div class="grey-foot"></div>
  <div class="cta">
    <h4>CALL TO SCHEDULE YOUR FREE CONSULTATION</h4>
    <div class="cta-row">
      <div class="cta-phone"><svg viewBox="0 0 24 24"><path fill="#1b1b1b" d="M6.6 10.8a15.1 15.1 0 0 0 6.6 6.6l2.2-2.2c.3-.3.7-.4 1-.2 1.1.4 2.3.6 3.6.6.6 0 1 .4 1 1V20c0 .6-.4 1-1 1A17 17 0 0 1 3 4c0-.6.4-1 1-1h3.5c.6 0 1 .4 1 1 0 1.3.2 2.5.6 3.6.1.3 0 .7-.2 1z"/></svg>805 419 2276</div>
      <div class="cta-links">office@covelinesmiles.com<br>www.covelinesmiles.com</div>
    </div>
  </div>
</section>

</body>
</html>
```